Design a Flyer for Fitness Business

Hi All

Contest for a sales flyer for an online fitness business, main sales points:

- grow your business -> reach new customers
- Increase revenue -> Fill the off peak classes
- reach a new market -> increase market and brand exposure

There will be some minor changes required after the winner is announced. We need something modern and in line with our website design.

Thankyou!

```html
<!DOCTYPE html>
<html lang="en">
<head>
<meta charset="utf-8">
<title>Vigora Fitness Business Flyer</title>
<link rel="stylesheet" href="https://fonts.googleapis.com/css2?family=Open+Sans:wght@400;600;700&family=Oswald:wght@600&display=swap">
<style>
  :root {
    --orange: #f7941d;
    --dark-soft: #454545;
    --white: #ffffff;
    --ink: #333333;
    --ink-soft: #444444;
    --page: #e4e4e4;
  }
  * { margin: 0; padding: 0; box-sizing: border-box; }
  html, body {
    width: 1200px; height: 1200px; overflow: hidden;
    background: var(--page);
    font-family: "Open Sans", Arial, sans-serif;
  }
  .canvas { position: relative; width: 1200px; height: 1200px; }
  .flyer {
    position: absolute; left: 160px; top: 30px;
    width: 880px; height: 1140px; overflow: hidden;
    background: var(--white);
    box-shadow: 0 6px 24px rgba(0,0,0,0.25);
  }
  .flyer-shapes { position: absolute; inset: 0; width: 100%; height: 100%; }
  .brand-name {
    position: absolute; left: 52px; top: 46px;
    font-weight: 600; font-size: 54px; line-height: 1;
    color: var(--white); letter-spacing: 1px;
  }
  .hero-title {
    position: absolute; left: 141px; top: 308px;
    font-family: "Oswald", "Arial Narrow", sans-serif;
    font-weight: 600; font-size: 40px; line-height: 1;
    color: var(--white); letter-spacing: 0.5px;
  }
  .hero-tagline {
    position: absolute; left: 141px; top: 356px;
    font-size: 20px; color: var(--white); line-height: 1;
  }
  .hero-tagline .accent { color: var(--orange); font-weight: 700; }
  .intro { position: absolute; left: 56px; top: 488px; width: 335px; color: var(--white); }
  .intro-title { font-size: 21px; font-weight: 400; line-height: 1; margin-bottom: 14px; }
  .intro-title strong { font-weight: 700; }
  .intro-text { font-size: 14px; line-height: 19.5px; }
  .feature { position: absolute; }
  .feature-title { font-size: 18px; font-weight: 600; line-height: 1; margin-bottom: 10px; color: var(--ink); }
  .feature-text { font-size: 14px; line-height: 19px; color: var(--ink-soft); }
  .feature--growth { left: 588px; top: 670px; width: 225px; }
  .feature--revenue { left: 59px; top: 756px; width: 300px; }
  .feature--market { left: 590px; top: 888px; width: 225px; }
  .contact {
    position: absolute; top: 1077px; display: flex; align-items: center; gap: 10px;
    font-size: 19px; color: var(--ink-soft);
  }
  .contact--phone { left: 398px; }
  .contact--email { left: 628px; }
  .contact-icon { width: 26px; height: 26px; }
</style>
</head>
<body>
<div class="canvas">
  <div class="flyer">
    <svg class="flyer-shapes" viewBox="0 0 555 718" preserveAspectRatio="none">
      <defs>
        <linearGradient id="darkFill" x1="0" y1="0" x2="0.3" y2="1">
          <stop offset="0" stop-color="#3c3c3c"/>
          <stop offset="1" stop-color="#1c1c1c"/>
        </linearGradient>
        <radialGradient id="athleteTone" cx="0.6" cy="0.4" r="0.65">
          <stop offset="0" stop-color="#8a8a8a"/>
          <stop offset="0.55" stop-color="#505050"/>
          <stop offset="1" stop-color="#2e2e2e" stop-opacity="0"/>
        </radialGradient>
        <linearGradient id="classTone" x1="0" y1="0" x2="1" y2="1">
          <stop offset="0" stop-color="#d9d4ce"/>
          <stop offset="0.5" stop-color="#b76b5a"/>
          <stop offset="1" stop-color="#5b5e66"/>
        </linearGradient>
        <linearGradient id="ballTone" x1="0" y1="0" x2="1" y2="1">
          <stop offset="0" stop-color="#cfd8e4"/>
          <stop offset="0.55" stop-color="#4f7fc9"/>
          <stop offset="1" stop-color="#2a4f9a"/>
        </linearGradient>
        <linearGradient id="groupTone" x1="0" y1="1" x2="1" y2="0">
          <stop offset="0" stop-color="#e8c64a"/>
          <stop offset="0.45" stop-color="#b98465"/>
          <stop offset="1" stop-color="#ffffff"/>
        </linearGradient>
        <linearGradient id="dividerFade" x1="0" y1="0" x2="1" y2="0">
          <stop offset="0" stop-color="#333" stop-opacity="0"/>
          <stop offset="0.5" stop-color="#333" stop-opacity="0.9"/>
          <stop offset="1" stop-color="#333" stop-opacity="0"/>
        </linearGradient>
      </defs>

      <rect class="dark-field" x="0" y="0" width="555" height="718" fill="url(#darkFill)"/>

      <rect class="athlete-photo" x="230" y="0" width="325" height="330" fill="url(#athleteTone)"
            role="img" aria-label="Black and white photo of a muscular man doing a push-up on his fists"/>

      <polygon class="stripe-orange" points="0,150 360,0 445,0 0,200" fill="var(--orange)"/>
      <polygon class="stripe-white" points="0,210 455,0 468,0 0,223" fill="var(--white)"/>

      <polygon class="light-field" points="0,457 345,375 555,442 555,718 0,718" fill="var(--white)"/>

      <polygon class="wedge-orange" points="0,230 357,372 0,457" fill="var(--orange)"/>

      <rect class="group-photo" x="0" y="555" width="218" height="163" fill="url(#groupTone)"
            role="img" aria-label="Photo of smiling women doing floor exercises in a fitness class"/>

      <rect class="spin-photo" x="246" y="425" width="109" height="83" fill="url(#classTone)"
            stroke="#bbbbbb" stroke-width="0.8"
            role="img" aria-label="Photo of people riding bikes in an indoor cycling class"/>
      <rect class="ball-photo" x="246" y="564" width="109" height="84" fill="url(#ballTone)"
            stroke="#bbbbbb" stroke-width="0.8"
            role="img" aria-label="Photo of people exercising on blue gym balls"/>

      <rect class="divider" x="282" y="536" width="212" height="1.6" fill="url(#dividerFade)"/>

      <polygon class="bar-dark" points="226,704 384,704 380,717 222,717" fill="var(--dark-soft)"/>
      <polygon class="bar-orange" points="388,704 519,704 515,717 384,717" fill="var(--orange)"/>
    </svg>

    <div class="brand-name">vigora</div>

    <h1 class="hero-title">READY TO GROW?</h1>
    <p class="hero-tagline">Get <span class="accent">MORE</span> from your classes today</p>

    <section class="intro">
      <h2 class="intro-title"><strong>FITNESS</strong> BUSINESS</h2>
      <p class="intro-text">Vigora is the online platform built for gyms, studios and personal trainers. We put your classes in front of thousands of active people searching for their next workout, so you can focus on coaching while we help you fill every spot and grow.</p>
    </section>

    <section class="feature feature--growth">
      <h3 class="feature-title">GROW YOUR BUSINESS</h3>
      <p class="feature-text">Reach new customers every week. List your classes online and let people nearby discover, book and pay for sessions in a few taps, any time of the day.</p>
    </section>

    <section class="feature feature--revenue">
      <h3 class="feature-title">INCREASE REVENUE</h3>
      <p class="feature-text">Fill your off-peak classes. Offer quiet time slots to new members and turn empty spaces into steady extra income without adding staff.</p>
    </section>

    <section class="feature feature--market">
      <h3 class="feature-title">REACH A NEW MARKET</h3>
      <p class="feature-text">Increase market and brand exposure. Your studio is shown to a wide online audience, building a name that brings people back again and again.</p>
    </section>

    <div class="contact contact--phone">
      <svg class="contact-icon" viewBox="0 0 24 24" aria-hidden="true">
        <path d="M6.6 2.5l3 3.2-1.8 2.3c1.2 2.6 3.4 4.9 6.2 6.2l2.3-1.8 3.2 3-1.9 3.3C11 18.3 5.7 13 4.1 4.4z" fill="var(--orange)"/>
      </svg>
      <span>012340 556677</span>
    </div>
    <div class="contact contact--email">
      <svg class="contact-icon" viewBox="0 0 24 24" aria-hidden="true">
        <rect x="2" y="5" width="20" height="14" fill="var(--orange)"/>
        <polyline points="2,5 12,13 22,5" fill="none" stroke="var(--white)" stroke-width="1.6"/>
      </svg>
      <span>hello@vigora.com</span>
    </div>
  </div>
</div>
</body>
</html>
```